TRU PEAK POWER.

I'd like my business logo.
contact name: Desmond Halvik
phone:0438275160
email: info@trupeakpower.net.au
website: www.trupeakpower.net.au

services:
solar
battery storage
LED lighting
energy saving solutions
general electrical
I'd like the design to look professional

Target Market(s)

Everyone

Industry/Entity Type

Business

Contact Information for Business Card

as described above

Requirements
Must have
• Id like the colours and the design to work well with my logo.

```html
<!DOCTYPE html>
<html lang="en">
<head>
<meta charset="utf-8">
<title>Tru Peak Power – Business Card</title>
<link href="https://fonts.googleapis.com/css2?family=Arimo:wght@400;700&display=swap" rel="stylesheet">
<style>
  :root {
    --backdrop: #2b2b2b;
    --card-white: #ffffff;
    --card-shade: #ececec;
    --brand-green: #4a9a2c;
    --green-light: #6bb23f;
    --green-dark: #3f8a28;
    --green-deep: #2f7a22;
    --brand-orange: #e8760f;
    --ink: #1d1d1d;
    --ink-soft: #ffffff;
  }
  * { box-sizing: border-box; margin: 0; padding: 0; }
  html, body {
    width: 1200px; height: 997px; overflow: hidden;
    background: var(--backdrop);
    font-family: "Arimo", Arial, sans-serif;
  }
  .business-card {
    position: absolute; left: 150px; top: 241px;
    width: 900px; height: 514px;
    border-radius: 24px; overflow: hidden;
    background: linear-gradient(180deg, var(--card-white) 0%, var(--card-shade) 100%);
  }
  .card-swoosh { position: absolute; inset: 0; width: 900px; height: 514px; }
  .brand {
    position: absolute; left: 60px; top: 112px;
    display: flex; align-items: center; gap: 16px;
  }
  .brand-dot {
    width: 46px; height: 46px; border-radius: 50%;
    background: var(--brand-orange);
  }
  .brand-name {
    font-weight: 700; font-size: 40px; letter-spacing: 1px;
    color: var(--brand-green);
  }
  .services { position: absolute; left: 60px; top: 322px; }
  .services-title {
    font-weight: 700; font-style: italic; font-size: 22px;
    color: var(--brand-orange); margin-bottom: 8px;
  }
  .services-list { list-style: none; }
  .services-list li {
    font-size: 22px; line-height: 30px; color: var(--brand-green);
  }
  .contact-person {
    position: absolute; right: 44px; top: 74px; text-align: right;
  }
  .person-name { font-weight: 700; font-size: 21px; color: var(--ink); }
  .person-role { font-size: 15px; color: var(--ink-soft); margin-top: 2px; }
  .contact-details {
    position: absolute; right: 36px; top: 290px;
    list-style: none; text-align: right;
  }
  .contact-details li {
    display: flex; justify-content: flex-end; align-items: center;
    gap: 12px; font-size: 19px; color: var(--ink);
    line-height: 24px; margin-bottom: 20px;
  }
  .contact-icon { width: 20px; height: 20px; flex: none; }
</style>
</head>
<body>
  <section class="business-card">
    <svg class="card-swoosh" viewBox="0 0 900 514" aria-hidden="true">
      <defs>
        <linearGradient id="panelGreen" x1="0" y1="0" x2="1" y2="1">
          <stop offset="0" stop-color="#5fae52"/>
          <stop offset="0.5" stop-color="#6bb23f"/>
          <stop offset="1" stop-color="#4e9a2a"/>
        </linearGradient>
      </defs>
      <path d="M560 0 C470 130 520 380 300 514 L900 514 L900 0 Z" fill="var(--brand-orange)"/>
      <path d="M600 0 C505 130 555 380 335 514 L900 514 L900 0 Z" fill="var(--green-deep)"/>
      <path d="M640 0 C545 140 590 390 375 514 L900 514 L900 0 Z" fill="url(#panelGreen)"/>
    </svg>

    <div class="brand">
      <span class="brand-dot"></span>
      <span class="brand-name">TRU PEAK POWER</span>
    </div>

    <div class="services">
      <h2 class="services-title">Our Services</h2>
      <ul class="services-list">
        <li>Solar</li>
        <li>LED lighting</li>
        <li>Battery storage</li>
        <li>Energy saving solutions</li>
      </ul>
    </div>

    <div class="contact-person">
      <p class="person-name">Desmond Halvik</p>
      <p class="person-role">Chairman</p>
    </div>

    <ul class="contact-details">
      <li>0438275160
        <svg class="contact-icon" viewBox="0 0 20 20" aria-hidden="true"><rect width="20" height="20" rx="5" fill="#e6e6e6"/><path d="M6 5h2l1 3-1.4 1a7 7 0 0 0 3.4 3.4L12 11l3 1v2c0 .6-.4 1-1 1A10 10 0 0 1 5 6c0-.6.4-1 1-1z" fill="#555"/></svg>
      </li>
      <li>info@trupeakpower.net.au
        <svg class="contact-icon" viewBox="0 0 20 20" aria-hidden="true"><rect width="20" height="20" rx="5" fill="#e6e6e6"/><rect x="4" y="6" width="12" height="8" fill="none" stroke="#555" stroke-width="1.5"/><path d="M4 6l6 5 6-5" fill="none" stroke="#555" stroke-width="1.5"/></svg>
      </li>
      <li>www.trupeakpower.net.au
        <svg class="contact-icon" viewBox="0 0 20 20" aria-hidden="true"><rect width="20" height="20" rx="5" fill="#e6e6e6"/><circle cx="10" cy="10" r="5.5" fill="none" stroke="#555" stroke-width="1.5"/><path d="M4.5 10h11M10 4.5c-2.5 3-2.5 8 0 11M10 4.5c2.5 3 2.5 8 0 11" fill="none" stroke="#555" stroke-width="1.2"/></svg>
      </li>
    </ul>
  </section>
</body>
</html>
```